TLPB Business Card Design

Business card for sole operator professional civil and traffic engineer.
Clients are developers and planners who require assistance with traffic strategic master planning advice and design development for access and infrastructure associated with the development.
Colours already in use are greens for the business name and black for other legend. The attached file shows the letterhead template which is currently in use.
Target Market(s)
Professional Clients in development industry
Most clients known to the Principal and card is mostly required to allow ongoing contact
Industry/Entity Type
Business
Contact Information for Business Card
DESMOND HALVERTON CONSULTING SERVICES
ABN 37 818 502 194
PO Box 871 KERRAWAY NSW 2619
Desmond Halverton 0431 558 906
desmond.halverton@quillmarsh.net

```html
<!DOCTYPE html>
<html lang="en">
<head>
<meta charset="utf-8">
<title>Desmond Halverton Consulting Services – Business Card</title>
<link rel="stylesheet" href="https://fonts.googleapis.com/css2?family=Tinos&display=swap">
<style>
  :root {
    --paper: #ffffff;
    --ink: #000000;
    --brand-green: #7cf400;
    --rule-green: #7ee812;
  }
  html, body {
    margin: 0;
    padding: 0;
    overflow: hidden;
    background: var(--paper);
  }
  .card {
    position: relative;
    width: 1200px;
    height: 769px;
    background: var(--paper);
    font-family: "Tinos", "Times New Roman", serif;
    color: var(--ink);
    overflow: hidden;
  }
  .card__name {
    position: absolute;
    left: 366px;
    width: 416px;
    top: 174px;
    margin: 0;
    font-size: 48px;
    font-weight: 400;
    line-height: 1;
    text-align: center;
    white-space: nowrap;
  }
  .card__rule {
    position: absolute;
    left: 366px;
    top: 234px;
    width: 416px;
    height: 4px;
    background: var(--rule-green);
  }
  .card__details {
    margin: 0;
    padding: 0;
    list-style: none;
    font-size: 30px;
    line-height: 1;
  }
  .card__detail {
    position: absolute;
    white-space: nowrap;
  }
  .card__detail--abn    { left: 132px; top: 456px; }
  .card__detail--post   { left: 82px;  top: 506px; }
  .card__detail--mobile { left: 132px; top: 560px; }
  .card__detail--email  { left: 82px;  top: 616px; }
  .card__band {
    position: absolute;
    left: 1010px;
    top: 30px;
    width: 136px;
    height: 708px;
    background: var(--brand-green);
    display: flex;
    justify-content: center;
  }
  .card__business {
    writing-mode: vertical-rl;
    margin: 0;
    padding-top: 40px;
    font-size: 25px;
    font-weight: 400;
    line-height: 1;
    letter-spacing: 0.2px;
    white-space: nowrap;
  }
</style>
</head>
<body>
  <div class="card">
    <h1 class="card__name">Desmond Halverton</h1>
    <div class="card__rule"></div>

    <ul class="card__details">
      <li class="card__detail card__detail--abn">ABN 37 818 502 194</li>
      <li class="card__detail card__detail--post">PO Box 871 KERRAWAY NSW 2619</li>
      <li class="card__detail card__detail--mobile">Mobile: 0431 558 906</li>
      <li class="card__detail card__detail--email">Email: desmond.halverton@quillmarsh.net</li>
    </ul>

    <div class="card__band">
      <p class="card__business">DESMOND HALVERTON CONSULTING SERVICES</p>
    </div>
  </div>
</body>
</html>
```